KT Crewing business card

Require business card which includes:
Company name: KT CREWING PTY LTD
Email: Mick@ktcrewing.com.au
Phone: 0431 556 208
ACN: 517 238 649

slogan: Onsite Auto Electrician Labour hire

Details and logo on top side
Logo only on bottom side

colour codes : #F15A29 , #939598

Target Market(s)

Western Australia mining sector

Industry/Entity Type

Mining

Contact Information for Business Card

Require business card which includes: Company name: KT CREWING PTY LTD Email: Mick@ktcrewing.com.au Phone: 0431 556 208 ACN: 517 238 649 slogan: Onsite Auto Electrician Labour hire Details and logo on top side Logo only on bottom side colour codes : #F15A29 , #939598

Colors
EE7325
F08F49
F5BC92
FAE3D3
FDF4ED

Requirements
Must have
• double sided

```html
<!DOCTYPE html>
<html lang="en">
<head>
<meta charset="utf-8">
<title>KT Crewing business card</title>
<link rel="stylesheet" href="https://fonts.googleapis.com/css2?family=Roboto:wght@400;700;900&display=swap">
<style>
  :root {
    --orange: #F15A29;
    --orange-card: #DD5226;
    --orange-deep: #B4421D;
    --grey: #939598;
    --grey-text: #7d7f82;
    --paper: #f2f2f2;
    --backdrop: #2b2b2b;
  }
  * { box-sizing: border-box; margin: 0; padding: 0; }
  html, body {
    width: 1200px; height: 1138px; overflow: hidden;
    background: var(--backdrop);
    font-family: "Roboto", Arial, sans-serif;
  }
  .canvas { position: relative; width: 1200px; height: 1138px; }
  .card {
    position: absolute; left: 273px; width: 620px; height: 376px;
    border-radius: 16px; overflow: hidden;
  }
  .card--front { top: 184px; background: var(--orange-card); display: flex; align-items: center; justify-content: center; }
  .front-name {
    font-weight: 900; font-size: 92px; letter-spacing: -1px;
    color: var(--orange-deep); line-height: 1;
  }
  .card--back { top: 606px; background: var(--paper); }
  .brand {
    position: absolute; left: 34px; top: 60px;
    display: flex; align-items: center; gap: 16px;
  }
  .brand-mark { width: 46px; height: 46px; background: var(--grey); }
  .brand-name {
    font-weight: 900; font-size: 66px; color: var(--orange);
    line-height: 1; letter-spacing: -1px;
  }
  .person { position: absolute; left: 34px; top: 218px; }
  .person-name { font-weight: 700; font-size: 24px; color: var(--orange); line-height: 1.1; }
  .person-role { font-size: 17px; color: var(--grey-text); margin-top: 3px; }
  .acn { position: absolute; left: 34px; top: 309px; font-size: 17px; color: var(--grey-text); }
  .acn-label { color: var(--orange); }
  .contacts { position: absolute; left: 334px; top: 218px; list-style: none; }
  .contacts li {
    display: flex; align-items: center; gap: 16px;
    height: 24px; font-size: 17px; color: var(--grey-text);
  }
  .contacts svg { width: 16px; height: 16px; fill: var(--orange); flex: none; }
  .strip-grey { position: absolute; left: 0; right: 0; bottom: 0; height: 15px; background: #a9abae; }
  .slogan-band {
    position: absolute; left: 263px; right: 0; bottom: 0; height: 48px;
    background: var(--orange);
    clip-path: polygon(27px 0, 100% 0, 100% 100%, 0 100%);
    display: flex; align-items: center; justify-content: flex-end; padding-right: 27px;
    color: #fff; font-size: 17px;
  }
</style>
</head>
<body>
<div class="canvas">
  <section class="card card--front">
    <span class="front-name">KT Crewing</span>
  </section>

  <section class="card card--back">
    <div class="brand">
      <span class="brand-name">KT Crewing</span>
      <span class="brand-mark"></span>
    </div>

    <div class="person">
      <p class="person-name">Tobias Mick</p>
      <p class="person-role">Managing Director</p>
    </div>

    <p class="acn"><span class="acn-label">ACN:</span> 517 238 649</p>

    <ul class="contacts">
      <li>
        <svg viewBox="0 0 16 16" aria-hidden="true"><path d="M2 5c0-2 3-3 6-3s6 1 6 3v1h-3V5H5v1H2z M4 7h8l2 7H2z M8 9a2 2 0 1 0 0.01 0z"/></svg>
        0431 556 208
      </li>
      <li>
        <svg viewBox="0 0 16 16" aria-hidden="true"><path d="M1 3h14v10H1z M2 4l6 5 6-5v1L8 10 2 5z" fill-rule="evenodd"/></svg>
        Mick@ktcrewing.com.au
      </li>
      <li>
        <svg viewBox="0 0 16 16" aria-hidden="true"><path d="M8 1a7 7 0 1 0 0.01 0z M3 8h10 M8 2v12" /><circle cx="8" cy="8" r="7"/><path d="M1.5 7.3h13v1.4h-13z M7.3 1.5h1.4v13H7.3z" fill="#f2f2f2"/></svg>
        www.ktcrewing.com.au
      </li>
    </ul>

    <div class="strip-grey"></div>
    <div class="slogan-band">Onsite Auto Electrician Labour Hire</div>
  </section>
</div>
</body>
</html>
```